EV Charging Station Integrator needs a website for Tremiq

We need a website to inform our customers and partners of what we do. At Tremiq, we plan, design, and deploy EVcharging Solutions as a Service by leveraging a best-in-class multi-vendor and partner network with expertise to deliver EV Hardware, Software and Services as Turn-Key and Agnostic solutions.

The website should have 3 pages + contact (HOME, THE PROBLEM, THE SOLUTION) + Contact information. Please see PPT attached for suggested framework.

```html
<!DOCTYPE html>
<html lang="en">
<head>
<meta charset="utf-8">
<title>Tremiq EV Charging</title>
<link href="https://fonts.googleapis.com/css2?family=Krona+One&family=Lato:wght@400;700;900&display=swap" rel="stylesheet">
<style>
:root{
  --navy:#231c4a;
  --navy-soft:rgba(45,38,92,.86);
  --orange:#ff8a00;
  --amber:#ffb400;
  --text:#2b2b2b;
  --muted:#4a4a4a;
  --light:#f5f5f5;
  --white:#ffffff;
}
*{margin:0;padding:0;box-sizing:border-box}
html,body{width:1200px;height:2214px;overflow:hidden}
body{position:relative;font-family:'Lato',sans-serif;color:var(--text);background:var(--white)}
.abs{position:absolute}
.display{font-family:'Krona One',sans-serif}

/* top bar */
.topbar{left:0;top:0;width:1200px;height:32px;background:var(--navy);color:var(--white);font-size:10px;font-weight:700;display:flex;align-items:center}
.topbar .item{position:absolute;display:flex;align-items:center;gap:4px;top:10px}
.topbar .divider{position:absolute;top:6px;width:1px;height:20px;background:var(--white)}
.social{position:absolute;top:8px;left:954px;display:flex;gap:6px}
.social span{width:15px;height:15px;border:1.5px solid var(--white);border-radius:50%}

/* header */
.header{left:0;top:32px;width:1200px;height:63px;background:var(--white)}
.brand{left:162px;top:18px;display:flex;align-items:center;gap:10px;font-family:'Krona One',sans-serif;font-size:26px;color:var(--navy);letter-spacing:4px}
.brand .dot{width:26px;height:26px;border-radius:50%;background:var(--orange)}
.nav{top:27px;font-size:11px;font-weight:900;color:var(--navy)}
.nav.active{color:var(--orange)}
.nav.active::after{content:"";display:block;width:28px;height:3px;background:var(--orange);border-radius:2px;margin-top:4px}
.btn{background:linear-gradient(90deg,var(--amber),var(--orange));color:var(--white);font-family:'Krona One',sans-serif;border-radius:12px 0 12px 0;display:flex;align-items:center;justify-content:center}
.btn.contact{left:913px;top:15px;width:124px;height:35px;font-size:10px}

/* hero */
.hero-photo{left:0;top:95px;width:1200px;height:560px;background:linear-gradient(120deg,#9cc4e8 0%,#3b7fc0 30%,#0f3f7a 55%,#cfd6de 75%,#1c2434 100%)}
.hero-panel{left:0;top:196px;width:602px;height:287px;background:var(--navy-soft);border-radius:0 8px 8px 0}
.hero-kicker{left:101px;top:246px;font-size:16px;color:var(--amber)}
.hero-title{left:101px;top:272px;font-size:31px;line-height:38px;color:var(--white)}
.hero-title em{font-style:normal;color:var(--amber)}
.btn.start{left:101px;top:394px;width:124px;height:34px;font-size:10px}

/* why choose */
.kicker{width:1200px;left:0;text-align:center;font-size:15px;color:var(--amber)}
.section-title{width:1200px;left:0;text-align:center;font-size:31px;color:var(--orange)}
.charger{left:0;top:800px;width:146px;height:531px;background:linear-gradient(90deg,#3a3a3a,#cfcfcf 55%,#eeeeee);border-radius:16px 30px 4px 4px}
.car{left:784px;top:1079px;width:416px;height:233px;background:radial-gradient(ellipse at 50% 55%,#f2f2f2 0%,#d8d8d8 55%,rgba(255,255,255,0) 72%)}
.vision-bg{left:0;top:1176px;width:1200px;height:250px;background:var(--light)}
.card{top:791px;width:271px;height:280px;background:var(--light);border-radius:14px;text-align:center;padding:0 12px}
.card.featured{background:var(--white);box-shadow:0 4px 22px rgba(0,0,0,.14);height:297px}
.card.featured::after{content:"";position:absolute;left:10px;right:10px;bottom:0;height:4px;border-radius:2px;background:linear-gradient(90deg,var(--amber),var(--orange))}
.card .icon{width:78px;height:78px;margin:23px auto 0;border:2px solid var(--orange);border-radius:6px;display:flex;align-items:center;justify-content:center}
.card.featured .icon{background:linear-gradient(135deg,var(--amber),var(--orange));border:none}
.card h3{font-size:15px;font-weight:900;color:var(--navy);margin-top:20px;line-height:20px}
.card p{font-size:11px;line-height:20px;color:var(--muted);margin-top:6px}

/* vision */
.vision-scene{left:0;top:1419px;width:1200px;height:395px;background:linear-gradient(180deg,#f5f5f5 0%,#9fb9b6 22%,#3f5a55 45%,#1f2a26 75%,#151b18 100%)}
.tent{left:352px;top:1540px;width:498px;height:216px;border-radius:249px 249px 0 0;background:radial-gradient(ellipse at 50% 40%,#ffd04a,#f3a51c 60%,#c97a10);opacity:.95}
.sub-title{font-size:13px;color:var(--orange)}
.vision-text{left:420px;top:1375px;width:360px;text-align:center;font-size:12.5px;line-height:20px;color:var(--text)}
.pillar{top:1635px;width:232px;text-align:center;color:var(--white)}
.pillar .sub-title{line-height:20px}
.pillar p{font-size:12.5px;line-height:20px;margin-top:6px}
.badge{width:94px;height:94px;border-radius:50%;display:flex;align-items:center;justify-content:center}
.badge.solid{background:linear-gradient(135deg,var(--amber),var(--orange));border:3px solid var(--white)}
.badge.ring{background:var(--white);box-shadow:inset 0 0 0 6px var(--white),inset 0 0 0 8px var(--amber)}

/* footer */
.footer{left:0;top:1790px;width:1200px;height:424px;background:var(--navy)}
.footer-brand{left:0;width:1200px;top:1945px;text-align:center;font-family:'Krona One',sans-serif;font-size:30px;letter-spacing:5px;color:var(--white)}
.footer-mark{left:580px;top:1880px;width:40px;height:40px;border-radius:50%;background:var(--orange)}
.footer-nav{left:0;width:1200px;top:2037px;display:flex;justify-content:center;gap:32px;font-size:11px;font-weight:900;color:var(--white)}
.rule{left:205px;width:790px;height:1px;background:rgba(255,255,255,.7)}
.footer-contact{top:2102px;font-size:10px;font-weight:700;color:var(--white);display:flex;align-items:center;gap:4px}
.vrule{top:2095px;width:1px;height:22px;background:var(--white)}
.copy{left:0;width:1200px;top:2169px;text-align:center;font-size:10px;font-weight:900;color:var(--white)}
.copy span{color:var(--amber);font-family:'Krona One',sans-serif;font-size:9px}
</style>
</head>
<body>

<!-- top bar -->
<div class="abs topbar">
  <div class="item" style="left:165px"><svg width="8" height="10" viewBox="0 0 8 10"><path d="M4 0a4 4 0 0 0-4 4c0 3 4 6 4 6s4-3 4-6a4 4 0 0 0-4-4zm0 5.5A1.5 1.5 0 1 1 4 2.5a1.5 1.5 0 0 1 0 3z" fill="#fff"/></svg>LOCATION : 123 LOREM IPSUM DOLOR SIT AMET</div>
  <div class="item" style="left:522px"><svg width="10" height="8" viewBox="0 0 10 8"><rect width="10" height="8" rx="1" fill="#fff"/><path d="M0 1l5 3.5L10 1" stroke="#231c4a" fill="none"/></svg>EMAIL ADDRESS : INFO@TREMIQ.COM</div>
  <div class="divider" style="left:727px"></div>
  <div class="item" style="left:748px"><svg width="10" height="10" viewBox="0 0 10 10"><path d="M2 0l2 2.5-1 1.5a6 6 0 0 0 3 3l1.5-1L10 8l-1.5 2C4 10 0 6 0 1.5z" fill="#fff"/></svg>CALL US TODAY : +1 888 888 8888</div>
  <div class="divider" style="left:937px"></div>
  <div class="social"><span></span><span></span><span></span><span></span></div>
</div>

<!-- header -->
<header class="abs header">
  <div class="abs brand"><span class="dot"></span>TREMIQ</div>
  <div class="abs nav active" style="left:626px">HOME</div>
  <div class="abs nav" style="left:690px">THE PROBLEM</div>
  <div class="abs nav" style="left:798px">THE SOLUTION</div>
  <div class="abs btn contact">CONTACT US</div>
</header>

<!-- hero -->
<section>
  <div class="abs hero-photo" role="img" aria-label="Electric car plugged into a charging station with glowing blue light streaks"></div>
  <div class="abs hero-panel"></div>
  <div class="abs hero-kicker">WELCOME TO TREMIQ EV CHARGING</div>
  <h1 class="abs hero-title display">ENABLING <em>FAST</em><br><em>AND INTEGRATED</em> EV<br>CHARGING NETWORKS.</h1>
  <div class="abs btn start">GET STARTED</div>
  <svg class="abs" style="left:0;top:560px" width="1200" height="110" viewBox="0 0 1200 110">
    <polygon points="0,85 110,55 295,27 470,52 600,85 725,50 907,22 1040,45 1200,85 1200,110 0,110" fill="#fff"/>
    <polyline points="110,55 295,27 470,52" fill="none" stroke="#ff8a00" stroke-width="6"/>
    <polyline points="725,50 907,22 1040,45" fill="none" stroke="#ff8a00" stroke-width="6"/>
  </svg>
</section>

<!-- why choose -->
<section>
  <div class="abs vision-bg"></div>
  <div class="abs kicker" style="top:705px">ABOUT TREMIQ</div>
  <h2 class="abs section-title display" style="top:726px">WHY CHOOSE US ?</h2>
  <div class="abs charger" role="img" aria-label="Wall-mounted EV charging station on a pedestal"></div>
  <div class="abs car" role="img" aria-label="White electric car"></div>

  <article class="abs card" style="left:163px">
    <div class="icon"><svg width="40" height="40" viewBox="0 0 40 40" fill="none" stroke="#ff8a00" stroke-width="2"><circle cx="20" cy="14" r="7"/><rect x="8" y="24" width="24" height="10"/></svg></div>
    <h3>BEST OF BREED ECOSYSTEM</h3>
    <p>We plan, design, and deploy EV(1) charging Solutions as a Service by leveraging a best-in-class multi-vendor and partner network with expertise to deliver EV Hardware, Software and Services as Turn-Key and Agnostic solutions.</p>
  </article>
  <article class="abs card featured" style="left:456px">
    <div class="icon"><svg width="40" height="40" viewBox="0 0 40 40" fill="none" stroke="#fff" stroke-width="2"><rect x="6" y="12" width="10" height="22"/><rect x="18" y="6" width="10" height="28"/><circle cx="31" cy="26" r="6"/></svg></div>
    <h3>SCALABILITY WITH LITTLE TO<br>NO INVESTMENT</h3>
    <p style="margin-top:0">We offer the ability to charge in minutes making for a scalable and nationwide application. The EV platform is delivered via consumption-based models allowing cities and enterprises to out-source the EV solution without prohibitive up-front investments</p>
  </article>
  <article class="abs card" style="left:748px">
    <div class="icon"><svg width="40" height="40" viewBox="0 0 40 40" fill="none" stroke="#ff8a00" stroke-width="2"><circle cx="20" cy="16" r="9"/><path d="M16 26v6h8v-6"/></svg></div>
    <h3>SUSTAINABLE INNOVATION</h3>
    <p>We enable a new, smart and high-power EV charging solution and consumer lifestyle powered by AI(2) with sustainability in mind. We incorporate solar and other CO2 reducing technologies into our solution platform to augment power-limited grids when needed</p>
  </article>
</section>

<!-- vision -->
<section>
  <div class="abs vision-scene" role="img" aria-label="Glowing tent in front of a misty mountain range at dusk"></div>
  <div class="abs tent" role="img" aria-label="Illuminated orange camping tent"></div>
  <h2 class="abs section-title display" style="top:1284px">OUR VISION</h2>
  <div class="abs display sub-title" style="left:0;width:1200px;text-align:center;top:1352px">SUSTAINABILITY</div>
  <p class="abs vision-text">Deploy citywide ESG(2) solutions that leverage green technology and help reduce carbon footprint, fossil fuel residue and harmful gas released back into the environment</p>

  <svg class="abs" style="left:0;top:1480px" width="1200" height="290" viewBox="0 0 1200 290">
    <path d="M333 282 C 340 120 450 20 600 10 C 750 20 860 120 871 282" fill="none" stroke="#ffb400" stroke-width="3" stroke-dasharray="12 8"/>
  </svg>
  <div class="abs badge solid" style="left:553px;top:1439px"><svg width="40" height="40" viewBox="0 0 40 40" fill="none" stroke="#fff" stroke-width="2"><circle cx="20" cy="14" r="8"/><path d="M6 32l8-6h12"/></svg></div>
  <div class="abs badge ring" style="left:298px;top:1634px"><svg width="40" height="40" viewBox="0 0 40 40" fill="none" stroke="#ff8a00" stroke-width="2"><rect x="8" y="6" width="16" height="28"/><path d="M24 14h6v14"/></svg></div>
  <div class="abs badge ring" style="left:811px;top:1634px"><svg width="40" height="40" viewBox="0 0 40 40" fill="none" stroke="#ff8a00" stroke-width="2"><circle cx="20" cy="14" r="8"/><path d="M6 32l8-6h12"/></svg></div>

  <div class="abs pillar" style="left:50px">
    <div class="display sub-title">EV(1) ANYWHERE &amp;<br>EVERYWHERE</div>
    <p>Enable access to EV charging stations on every city corner, interstate highways as well as rural and underserved areas.</p>
  </div>
  <div class="abs pillar" style="left:919px">
    <div class="display sub-title">FAST &amp; INTEGRATED<br>SOLUTION</div>
    <p>Provide high-power, open access EV charging networks and pay systems fueled by smart energy technologies</p>
  </div>
</section>

<!-- footer -->
<footer>
  <div class="abs footer"></div>
  <svg class="abs" style="left:0;top:1790px" width="1200" height="90" viewBox="0 0 1200 90">
    <polygon points="0,0 1200,0 1200,5 907,82 600,5 295,82 0,5" fill="#171c19"/>
    <polyline points="155,45 295,82 470,38" fill="none" stroke="#ff8a00" stroke-width="7"/>
    <polyline points="730,38 907,82 1085,35" fill="none" stroke="#ffb400" stroke-width="7"/>
  </svg>
  <div class="abs footer-mark"></div>
  <div class="abs footer-brand">TREMIQ</div>
  <nav class="abs footer-nav"><span>HOME</span><span>THE PROBLEM</span><span>THE SOLUTION</span><span>CONTACT US</span></nav>
  <div class="abs rule" style="top:2073px"></div>
  <div class="abs footer-contact" style="left:223px"><svg width="8" height="10" viewBox="0 0 8 10"><path d="M4 0a4 4 0 0 0-4 4c0 3 4 6 4 6s4-3 4-6a4 4 0 0 0-4-4z" fill="#fff"/></svg>LOCATION : 123 LOREM IPSUM DOLOR SIT AMET</div>
  <div class="abs vrule" style="left:496px"></div>
  <div class="abs footer-contact" style="left:537px"><svg width="10" height="8" viewBox="0 0 10 8"><rect width="10" height="8" rx="1" fill="#fff"/></svg>EMAIL ADDRESS : INFO@TREMIQ.COM</div>
  <div class="abs vrule" style="left:765px"></div>
  <div class="abs footer-contact" style="left:805px"><svg width="10" height="10" viewBox="0 0 10 10"><path d="M2 0l2 2.5-1 1.5a6 6 0 0 0 3 3l1.5-1L10 8l-1.5 2C4 10 0 6 0 1.5z" fill="#fff"/></svg>CALL US TODAY : +1 888 888 8888</div>
  <div class="abs rule" style="top:2140px"></div>
  <div class="abs copy">© COPYRIGHTS 2023 <span>TREMIQ EV CHARGING</span> &nbsp;|&nbsp;&nbsp;&nbsp; ALL RIGHTS RESERVED.</div>
</footer>

</body>
</html>
```